Real estate investor, needing a business card that communicates warmth, integrity, empathy.

I have a logo that can be manipulated to align with the message - "Serving your home selling needs." Want it to stand out from typical real estate investor cards, and make distressed home sellers feel a connection with me. Should communicate warmth, integrity, empathy, and trustworthiness.

Target Market(s)

Distressed home owners who need to sell their homes, not using realtors.

Contact Information for Business Card

Glossy front and matte back, with a small box that is labelled "notes." I like darker blues and blacks together, but doesn't have to be, as long as it communicates trustworthiness, and a strong call to action.

Other font styles liked:
• see "must haves" above, but willing to review whatever comes my way.

Requirements
Must have
• The fonts on my logo are Aviano, Lusitana, and Marcellus. We don't have to use those, but I favor them.

```html
<!DOCTYPE html>
<html lang="en">
<head>
<meta charset="UTF-8">
<title>Crestline Home Buyers – Business Card</title>
<link rel="stylesheet" href="https://fonts.googleapis.com/css2?family=Open+Sans:wght@400;600&family=Oswald:wght@500&display=swap">
<style>
  :root {
    --backdrop: #2b2b2b;
    --card: #2f2f30;
    --ink: #f2f2f2;
    --ink-soft: #d9d9d9;
    --accent: #1878c4;
    --divider: #8a8a8a;
  }
  * { box-sizing: border-box; margin: 0; padding: 0; }
  html, body { width: 1200px; height: 901px; overflow: hidden; }
  body {
    background: var(--backdrop);
    font-family: "Open Sans", Arial, sans-serif;
    color: var(--ink);
    display: flex;
    flex-direction: column;
    align-items: center;
    justify-content: center;
    gap: 26px;
  }
  .card {
    position: relative;
    width: 700px;
    height: 400px;
    background: var(--card);
    box-shadow: 0 6px 18px rgba(0,0,0,.45);
    overflow: hidden;
  }
  .card__band {
    position: absolute;
    left: 0; right: 0; bottom: 0;
    height: 8px;
    background: var(--accent);
  }

  /* Front */
  .card--front {
    display: flex;
    flex-direction: column;
    align-items: center;
    justify-content: center;
  }
  .brand {
    display: flex;
    align-items: center;
    gap: 14px;
    font-weight: 600;
    font-size: 40px;
    letter-spacing: 4px;
    text-transform: uppercase;
    color: var(--ink);
  }
  .brand__mark {
    width: 18px; height: 18px;
    background: var(--accent);
  }
  .brand-sub {
    margin-top: 6px;
    font-weight: 600;
    font-size: 22px;
    letter-spacing: 8px;
    text-transform: uppercase;
    color: var(--ink);
  }
  .tagline {
    position: absolute;
    bottom: 30px;
    width: 100%;
    text-align: center;
    font-size: 17px;
    letter-spacing: .5px;
    color: var(--ink-soft);
  }

  /* Back */
  .identity {
    position: absolute;
    left: 60px;
    top: 145px;
    width: 270px;
    text-align: right;
  }
  .identity__name {
    font-family: "Oswald", "Arial Narrow", sans-serif;
    font-weight: 500;
    font-size: 40px;
    line-height: 1;
    text-transform: uppercase;
    color: var(--accent);
  }
  .identity__role {
    margin-top: 4px;
    font-size: 19px;
    color: var(--ink-soft);
  }
  .divider {
    position: absolute;
    left: 350px;
    top: 140px;
    width: 1px;
    height: 90px;
    background: var(--divider);
  }
  .contacts {
    position: absolute;
    left: 372px;
    top: 140px;
    list-style: none;
    display: flex;
    flex-direction: column;
    gap: 8px;
  }
  .contacts__item {
    display: flex;
    align-items: center;
    gap: 12px;
    font-size: 19px;
    color: var(--ink);
  }
  .contacts__item svg { width: 18px; height: 18px; flex: none; }
  .contacts__highlight { color: var(--accent); }
  .address {
    position: absolute;
    bottom: 34px;
    width: 100%;
    text-align: center;
    font-size: 20px;
    color: var(--ink);
  }
</style>
</head>
<body>

  <section class="card card--front">
    <div class="brand"><span class="brand__mark"></span>Crestline</div>
    <div class="brand-sub">Home Buyers</div>
    <p class="tagline">Serving your home selling needs</p>
    <div class="card__band"></div>
  </section>

  <section class="card card--back">
    <div class="identity">
      <h1 class="identity__name">Daniel Harper</h1>
      <p class="identity__role">Manager</p>
    </div>
    <div class="divider"></div>
    <ul class="contacts">
      <li class="contacts__item">
        <svg viewBox="0 0 24 24" fill="var(--accent)"><path d="M6.6 10.8a15.5 15.5 0 0 0 6.6 6.6l2.2-2.2a1 1 0 0 1 1-.25 11.4 11.4 0 0 0 3.6.57 1 1 0 0 1 1 1V20a1 1 0 0 1-1 1A17 17 0 0 1 3 4a1 1 0 0 1 1-1h3.5a1 1 0 0 1 1 1c0 1.25.2 2.45.57 3.6a1 1 0 0 1-.25 1z"/></svg>
        555-014-2100
      </li>
      <li class="contacts__item">
        <svg viewBox="0 0 24 24" fill="none" stroke="var(--accent)" stroke-width="2"><rect x="3" y="5" width="18" height="14" rx="1"/><path d="M3 6l9 7 9-7"/></svg>
        hello@crestlinehomes.com
      </li>
      <li class="contacts__item">
        <svg viewBox="0 0 24 24" fill="none" stroke="var(--accent)" stroke-width="2"><circle cx="12" cy="12" r="9"/><path d="M3 12h18M12 3c3 3 3 15 0 18M12 3c-3 3-3 15 0 18"/></svg>
        <span>www.<span class="contacts__highlight">crestlinehomes</span>.com</span>
      </li>
    </ul>
    <p class="address">Your address, city, state, ZIP 0000</p>
    <div class="card__band"></div>
  </section>

</body>
</html>
```